Law firm needs stationary and envelope design*

We would like to incorporate our logo into letterhead design and envelopes. We are looking for something that is moderately conservative but not old law firm style. Both the envelopes and the letterhead must have both firm addresses. We would like to incorporate the color of the logo, but only a small amount of color - perhaps on one of the borders. The addresses for the firm locations are listed below. Given that it is a law firm, it needs to somewhat conservative, but not the old school, small black font on cream colored paper design.

The firm addresses are:

27815 N. Harlow Pemberton Pkwy.
Ste 740
Scottsdale, AZ 85419

6208 E. Juniper Street
Ste 820
Burbank, CA 91873

Legal

Designer to choose colors to be used in the design.

• Both addresses:
• 27815 N. Harlow Pemberton Pkwy.
• Ste 740
• Scottsdale, AZ 85419
• 6208 E. Juniper Street
• Ste 820
• Burbank, CA 91873
• Small amount of color on border(s) that matches the logo but not too much color

```html
<!DOCTYPE html>
<html lang="en">
<head>
<meta charset="utf-8">
<title>Halvern Law — Letterhead &amp; Envelope</title>
<link rel="stylesheet" href="https://fonts.googleapis.com/css2?family=Mulish:ital,wght@0,400;0,600;1,400&display=swap">
<style>
  :root {
    --backdrop: #ececec;
    --paper: #fdf8ea;
    --flap: #e5e3dc;
    --navy: #2e2a6b;
    --ink: #2b2b2b;
    --muted: #6b6b6b;
    --rule: #8a8a8a;
    --mark-faint: #e6e0d0;
    --mark-grey: #9b9b9b;
    --sign-fill: #ece6d6;
  }
  * { margin: 0; padding: 0; box-sizing: border-box; }
  html, body {
    width: 1200px;
    height: 896px;
    overflow: hidden;
    background: var(--backdrop);
    font-family: "Mulish", "Avenir Next", Arial, sans-serif;
    color: var(--ink);
  }
  .stage { position: relative; width: 1200px; height: 896px; }

  /* Letterhead */
  .letterhead {
    position: absolute;
    left: 130px; top: 135px;
    width: 461px; height: 600px;
    background: var(--paper);
    overflow: hidden;
  }
  .firm-name {
    font-family: "Mulish", "Avenir Next", Arial, sans-serif;
    font-weight: 400;
    color: var(--navy);
    letter-spacing: 0.04em;
    white-space: nowrap;
  }
  .letterhead .firm-name {
    position: absolute;
    left: 52px; top: 42px;
    font-size: 26px;
  }
  .address {
    position: absolute;
    top: 110px;
    font-size: 9.5px;
    line-height: 12.5px;
    color: var(--muted);
    font-style: normal;
  }
  .address--scottsdale { left: 52px; }
  .address--burbank { right: 41px; text-align: right; }
  .header-rule {
    position: absolute;
    left: 52px; top: 150px;
    width: 368px; height: 1px;
    background: var(--rule);
  }
  .watermark {
    position: absolute;
    left: 150px; top: 330px;
    font-size: 36px;
    color: var(--mark-faint);
    transform: rotate(-43deg);
    transform-origin: left center;
  }
  .letter-body {
    position: absolute;
    left: 119px; top: 226px;
    width: 314px;
    font-size: 7.3px;
    line-height: 10.4px;
    color: var(--ink);
  }
  .letter-body p { text-indent: 10px; margin-bottom: 3px; }
  .closing {
    position: absolute;
    left: 130px; top: 440px;
    font-size: 13px;
    font-style: italic;
    color: var(--ink);
  }
  .signature {
    position: absolute;
    left: 118px; top: 468px;
    width: 181px; height: 47px;
    background: var(--sign-fill);
    border-radius: 4px;
  }
  .footer-web {
    position: absolute;
    left: 35px; top: 559px;
    font-size: 9px;
    color: var(--ink);
  }
  .footer-bar {
    position: absolute;
    left: 139px; top: 562px;
    right: 0; height: 5px;
    background: var(--navy);
  }

  /* Envelope */
  .envelope {
    position: absolute;
    left: 648px; top: 114px;
    width: 485px; height: 632px;
    background: var(--paper);
    overflow: hidden;
  }
  .envelope-flap {
    position: absolute;
    left: 0; top: 0;
    width: 485px; height: 74px;
  }
  .envelope .firm-name--flap {
    position: absolute;
    left: 243px; top: 20px;
    font-size: 24px;
  }
  .envelope .firm-name--spine {
    position: absolute;
    left: 50px; top: 523px;
    font-size: 44px;
    color: var(--mark-grey);
    transform: rotate(-90deg);
    transform-origin: left top;
    letter-spacing: 0.03em;
  }
</style>
</head>
<body>
<main class="stage">

  <section class="letterhead" aria-label="Letterhead">
    <div class="firm-name">HALVERN LAW</div>

    <address class="address address--scottsdale">
      27815 N. Harlow Pemberton Pkwy.<br>
      Ste 740<br>
      Scottsdale, AZ 85419
    </address>
    <address class="address address--burbank">
      6208 E. Juniper Street<br>
      Ste 820<br>
      Burbank, CA 91873
    </address>
    <div class="header-rule"></div>

    <div class="firm-name watermark" aria-hidden="true">HALVERN LAW</div>

    <div class="letter-body">
      <p>Thank you for choosing our firm to represent you in this matter. We have reviewed the documents you provided and prepared a short summary of the next steps. Please read the enclosed notes carefully and contact our office with any questions before the date listed below.</p>
      <p>Our attorneys will begin the initial review this week and will keep you informed at each stage of the process. We expect to file the first set of papers within thirty days, once all signed forms have been returned to us. During this period it is important that you keep copies of every letter, invoice and notice you receive, and share them with our team as soon as possible. Meetings may be held at either of our offices or by phone, whichever suits your schedule best. Fees will be billed monthly, and each statement will list the work completed and the time spent on it. If your circumstances change in any way, please let us know promptly so that we can adjust our approach. We look forward to working with you and to reaching a fair outcome.</p>
    </div>

    <div class="closing">Yours faithfully</div>
    <div class="signature" role="img" aria-label="Handwritten signature"></div>

    <div class="footer-web">www.halvernlaw.com</div>
    <div class="footer-bar"></div>
  </section>

  <section class="envelope" aria-label="Envelope">
    <svg class="envelope-flap" viewBox="0 0 485 74" aria-hidden="true">
      <path d="M0 0 H485 V74 H40 Q8 74 4 44 Z" fill="var(--flap)"/>
    </svg>
    <div class="firm-name firm-name--flap">HALVERN LAW</div>
    <div class="firm-name firm-name--spine">HALVERN LAW</div>
  </section>

</main>
</body>
</html>
```